Business Card Design Project

I require a business card for a new coaching business based in Melbourne with global clients. Both companies and individuals will retain our coaching services.

Target Market(s)

Both small business and large corporate in western speaking countries. Individuals requiring support and direction on issues such as fears, phobias, career, relationships, confidence, self esteem etc.

Industry/Entity Type

Business

Font styles to use
Sans Serif

Colors

Designer to choose colors to be used in the design.

Requirements
Must have
• White background to enhance the colours in the logo. Logo on the left.
Should not have
• The black and white version of the logo. Keep the colours.

```html
<!DOCTYPE html>
<html lang="en">
<head>
<meta charset="utf-8">
<title>Clear Path Coaching – Business Card</title>
<link rel="stylesheet" href="https://fonts.googleapis.com/css2?family=Open+Sans:wght@400;700&display=swap">
<style>
  :root {
    --backdrop: #e8e5e1;
    --card: #ffffff;
    --ink: #3f3f3f;
    --ink-soft: #5a5a5a;
    --label: #1a8fe3;
    --accent: #f5821f;
  }
  html, body {
    margin: 0;
    width: 1200px;
    height: 1045px;
    overflow: hidden;
    background: var(--backdrop);
    font-family: "Open Sans", Arial, sans-serif;
  }
  .card {
    position: absolute;
    left: 258px;
    width: 697px;
    height: 401px;
    background: var(--card);
    box-shadow: 0 2px 6px rgba(0,0,0,0.18);
  }
  .card--front { top: 80px; }
  .card--back  { top: 521px; }

  .brand {
    position: absolute;
    display: flex;
    align-items: center;
    gap: 16px;
  }
  .brand__dot {
    width: 62px;
    height: 62px;
    border-radius: 50%;
    background: var(--accent);
    flex: none;
  }
  .brand__name {
    margin: 0;
    font-weight: 700;
    font-size: 29px;
    line-height: 29px;
    letter-spacing: -0.5px;
    color: var(--ink);
    text-transform: uppercase;
  }
  .card--front .brand { left: 40px; top: 52px; }
  .card--back .brand { left: 50%; top: 50%; transform: translate(-50%, -50%); }

  .person {
    position: absolute;
    left: 373px;
    top: 64px;
  }
  .person__name {
    margin: 0;
    font-size: 22px;
    font-weight: 700;
    color: var(--ink);
  }
  .person__role {
    margin: 4px 0 0;
    font-size: 17px;
    color: var(--ink-soft);
  }

  .contact {
    position: absolute;
    left: 40px;
    top: 238px;
    margin: 0;
    font-style: normal;
    font-size: 17.5px;
    line-height: 25.5px;
    color: var(--ink-soft);
  }
  .contact__label {
    font-weight: 700;
    color: var(--label);
  }
</style>
</head>
<body>
  <section class="card card--front">
    <div class="brand">
      <span class="brand__dot"></span>
      <p class="brand__name">Clear Path<br>Coaching</p>
    </div>
    <div class="person">
      <p class="person__name">Maren Holloway</p>
      <p class="person__role">Performance Consultant and Coach</p>
    </div>
    <address class="contact">
      2190 Harbour Lane Suite 12<br>
      Fernvale, VIC 3999<br>
      <span class="contact__label">Phone:</span> +61 (0) 400 555 019<br>
      <span class="contact__label">ABN:</span> 00123456789<br>
      <span class="contact__label">Email:</span> maren@clearpathmail.com
    </address>
  </section>

  <section class="card card--back">
    <div class="brand">
      <span class="brand__dot"></span>
      <p class="brand__name">Clear Path<br>Coaching</p>
    </div>
  </section>
</body>
</html>
```